Redesign Gearcrate.co.uk website for Film,Tv & Photo Industries.

www.gearcrate.co.uk needs a major redesign and new fresh look.
We will be using Quillbrook V1 software and have a company that will do all the coding etc etc.

The website is for people who work in the film, tv and photographic industries and are looking to buy bags and cases for their equipment.
About 14 different Manufacturers will be featured.
Just need a modern home page, everything else will follow this design.
Updates

Hi All, I have altered the description of the project , not that much has altered just giving more info out. regards Rob Calder.

Hi Everyone, I have just uploaded a new logo for the www.gearcrate.co.uk website. regards Rob Calder.

Final logo has been uploaded. Regards Rob.

Reason: Even though there are many good designs a lot of them are the same. I would like to see even more of a modern design even using flat colours that don't follow the colour of the new logo regards Rob.

Having seen many very good designs I would like to see different designs using FLAT colours which are modern . You don't have to stick to the colours of the logo as i can change the red in the logo to match the colour of the website. regards Rob Calder.

Target Market(s)

Artistic People who work in Film , TV and photographic Industries. Photographers, cameramen, Production Companies who need to protect their equipment.
Both Pro and Amateur.

Industry/Entity Type

Software

Requirements
Must have
• open minded
Nice to have
• Modern Look

```html
<!DOCTYPE html>
<html lang="en">
<head>
<meta charset="utf-8">
<title>Gearcrate – Bags and Cases for Film, TV &amp; Photo</title>
<link rel="stylesheet" href="https://fonts.googleapis.com/css2?family=Arimo:wght@400;700&family=Dosis:wght@500;600&family=Jura:wght@600;700&display=swap">
<style>
:root{
  --ink:#2b2b2b;
  --ink-soft:#3a3a3a;
  --orange:#f47a3a;
  --orange-text:#f26a2a;
  --page:#f4f4f4;
  --panel:#ffffff;
  --line:#e2e2e2;
  --text:#555555;
  --muted:#9a9a9a;
}
*{box-sizing:border-box;margin:0;padding:0}
html,body{width:1200px;height:2206px;overflow:hidden}
body{background:var(--page);font-family:Arimo,Arial,sans-serif;color:var(--text);position:relative}
a{color:inherit;text-decoration:none}
ul{list-style:none}

/* top utility bar */
.utility{height:34px;background:var(--ink);color:#ddd;font-size:12px}
.utility .wrap{width:1004px;margin:0 auto;display:flex;align-items:center;height:100%;padding:0 20px}
.utility .sep{margin:0 8px;color:#888}
.utility .search{margin-left:auto;width:186px;height:20px;background:#1c1c1c;border:1px solid #444;border-radius:3px;position:relative}
.utility .search svg{position:absolute;right:5px;top:3px}
.utility .account{margin-left:14px}

/* header */
.masthead{height:89px;background:#fff}
.masthead .wrap{width:1004px;margin:0 auto;display:flex;align-items:center;height:100%;padding:0 20px}
.brand{display:flex;align-items:center;gap:14px}
.brand-square{width:80px;height:56px;background:var(--ink);border-radius:4px}
.brand-name{font-family:Dosis,sans-serif;font-weight:600;font-size:40px;color:var(--ink);letter-spacing:1px}
.basket{margin-left:auto;width:226px;height:73px;background:#f0f0f0;border:1px solid #e0e0e0;border-radius:8px;display:flex;align-items:center;padding:0 14px;gap:12px;font-size:12px;line-height:18px;color:#666}

/* nav */
.nav{width:1004px;margin:0 auto;height:54px;background:var(--orange);display:flex;align-items:stretch}
.nav a{display:flex;align-items:center;gap:7px;padding:0 22px;color:#fff;font-family:Dosis,sans-serif;font-weight:600;font-size:15px;text-transform:uppercase}
.nav a.current{background:var(--ink-soft)}

/* layout */
.layout{position:absolute;top:196px;left:98px;width:1004px;display:flex;gap:20px}
.sidebar{width:282px;display:flex;flex-direction:column;gap:22px}
.main{width:702px}

/* sidebar blocks */
.side-block{background:var(--panel);border-radius:6px;box-shadow:0 2px 3px rgba(0,0,0,.15);overflow:hidden}
.side-head{height:54px;background:var(--ink);color:#fff;display:flex;align-items:center;gap:12px;padding:0 16px;font-family:Dosis,sans-serif;font-weight:600;font-size:21px}
.side-list li{height:38px;display:flex;align-items:center;padding:0 20px;font-size:14px;color:#666;border-bottom:1px solid var(--line)}
.side-list li:last-child{border-bottom:none}
.post{display:flex;gap:14px;padding:16px 14px;height:103px;border-bottom:1px solid var(--line)}
.post:last-child{border-bottom:none}
.post-thumb{width:80px;height:72px;flex:none;background:#ececec;border:1px solid #ddd;display:flex;align-items:center;justify-content:center;font-family:Dosis,sans-serif;font-size:20px;color:#bbb}
.post-title{color:var(--orange-text);font-size:13px;font-weight:700;margin-top:4px}
.post-excerpt{font-size:11px;line-height:17px;color:#aaa;margin-top:4px}

/* hero */
.hero{height:405px;border-radius:6px;overflow:hidden;position:relative;box-shadow:0 2px 3px rgba(0,0,0,.15)}
.hero-photo{position:absolute;inset:0;background:linear-gradient(100deg,#3d3f44 0%,#5e6167 35%,#8a9098 60%,#6d7682 80%,#3e4a5a 100%)}
.hero-shade{position:absolute;inset:0;background:linear-gradient(90deg,rgba(20,20,20,.55) 0%,rgba(20,20,20,.25) 45%,rgba(20,20,20,0) 70%)}
.hero-copy{position:absolute;left:24px;top:74px;color:#fff;width:330px}
.hero-title{font-family:Dosis,sans-serif;font-weight:600;font-size:31px;letter-spacing:.5px}
.hero-text{font-size:16px;line-height:27px;margin-top:12px;width:300px}
.hero-price{font-family:Dosis,sans-serif;font-weight:500;font-size:58px;color:var(--orange);margin-top:20px}
.hero-shop{display:flex;align-items:center;gap:10px;font-size:14px;margin-top:8px}

/* panels */
.panel{background:var(--panel);border-radius:6px;box-shadow:0 2px 3px rgba(0,0,0,.15)}
.intro{margin-top:22px;height:432px;padding:18px 12px;position:relative}
.intro h1{font-family:Dosis,sans-serif;font-weight:500;font-size:21px;color:#444;padding:0 0 12px 2px;border-bottom:1px solid var(--line)}
.intro p{font-size:13.5px;line-height:29px;color:#666;margin-top:8px;padding:0 2px}
.brand-list{margin-top:14px}
.brand-list li{font-size:12.5px;line-height:28.5px;color:#444;display:flex;align-items:center;gap:10px;padding-left:4px}
.delivery-badge{position:absolute;left:502px;top:226px;width:190px;height:100px;border-radius:8px;background:linear-gradient(90deg,#d82323 0%,#d82323 50%,#2b2b2b 100%)}

.featured{margin-top:15px;padding-bottom:20px}
.featured-head{height:54px;background:var(--ink);border-radius:6px 6px 0 0;color:#fff;display:flex;align-items:center;gap:12px;padding:0 14px;font-family:Dosis,sans-serif;font-weight:600;font-size:21px}
.product-grid{display:grid;grid-template-columns:repeat(3,216px);gap:29px 14px;padding:29px 12px 0}
.product{height:340px;border:1px solid #ddd;border-radius:3px;text-align:center;padding:14px 12px}
.product-photo{width:100%;height:150px;border-radius:4px;background:radial-gradient(ellipse at center,#55594f 0%,#3b3e38 45%,#ffffff 46%)}
.product-name{font-family:Arimo,sans-serif;font-weight:400;font-size:19px;color:#333;margin-top:16px}
.product-desc{font-size:12.5px;line-height:18px;color:#555;margin-top:8px}
.product-price{font-size:12.5px;color:#444;margin-top:12px}
.product-price span{color:var(--orange-text)}
.btn{display:inline-block;width:142px;height:34px;line-height:34px;background:var(--ink-soft);color:#fff;border-radius:6px;font-size:13px;margin-top:12px}

/* footer */
.footer{position:absolute;left:0;top:1929px;width:1200px;height:277px;background:var(--ink);color:#ddd}
.footer-inner{position:absolute;left:118px;top:26px;width:964px;height:205px}
.footer h3{font-family:Jura,sans-serif;font-weight:700;font-size:19px;letter-spacing:1.5px;color:#eee}
.footer-products{position:absolute;left:0;top:0;width:270px}
.footer-products li{font-size:13px;height:29px;line-height:29px;border-bottom:1px solid #3d3d3d;color:#cfcfcf}
.footer-products ul{margin-top:8px}
.footer-pay{position:absolute;left:316px;top:0}
.pay-strip{margin-top:10px;width:592px;height:44px;background:#fff;border-radius:2px;display:flex;align-items:center;gap:6px;padding:0 6px}
.pay-chip{height:32px;border-radius:3px}
.call{position:absolute;left:0;right:0;top:143px;text-align:center;padding-left:300px;font-family:Jura,sans-serif;font-weight:700;font-size:23px;letter-spacing:2px;color:#fff}
.footer-rule{position:absolute;left:118px;right:118px;top:230px;border-top:1px solid #4a4a4a}
.copyright{position:absolute;left:0;right:0;top:242px;text-align:center;font-size:11px;color:#bbb}
</style>
</head>
<body>

<div class="utility">
  <div class="wrap">
    <a href="#">Shipping &amp; Returns</a><span class="sep">|</span><a href="#">Advanced Search</a>
    <div class="search"><svg width="12" height="12" viewBox="0 0 12 12"><circle cx="5" cy="5" r="3.5" fill="none" stroke="#aaa" stroke-width="1.5"/><line x1="7.6" y1="7.6" x2="11" y2="11" stroke="#aaa" stroke-width="1.5"/></svg></div>
    <a class="account" href="#">My Account</a><span class="sep">|</span><a href="#">Checkout</a>
  </div>
</div>

<header class="masthead">
  <div class="wrap">
    <div class="brand"><span class="brand-square"></span><span class="brand-name">GEARCRATE</span></div>
    <div class="basket">
      <svg width="40" height="34" viewBox="0 0 40 34"><path d="M2 4h7l5 18h20l4-13H11" fill="none" stroke="#f47a3a" stroke-width="3" stroke-linejoin="round"/><path d="M12 9h26l-4 13H14z" fill="#f47a3a"/><circle cx="16" cy="29" r="3" fill="#f47a3a"/><circle cx="31" cy="29" r="3" fill="#f47a3a"/></svg>
      <div>Your basket is empty!<br>Total : £0 , Exc Vat</div>
    </div>
  </div>
</header>

<nav class="nav">
  <a class="current" href="#"><svg width="13" height="12" viewBox="0 0 13 12"><path d="M6.5 0L0 6h2v6h3.5V8h2v4H11V6h2z" fill="#fff"/></svg>Home</a>
  <a href="#"><svg width="11" height="12" viewBox="0 0 11 12"><circle cx="5.5" cy="3" r="3" fill="#fff"/><path d="M0 12c0-4 2.5-5.5 5.5-5.5S11 8 11 12z" fill="#fff"/></svg>My Account</a>
  <a href="#"><svg width="9" height="13" viewBox="0 0 9 13"><path d="M4.5 0A4.5 4.5 0 0 0 0 4.5C0 8 4.5 13 4.5 13S9 8 9 4.5A4.5 4.5 0 0 0 4.5 0z" fill="#fff"/><circle cx="4.5" cy="4.5" r="1.7" fill="#f47a3a"/></svg>Contact</a>
  <a href="#"><svg width="14" height="12" viewBox="0 0 14 12"><path d="M0 1h3l2 7h7l2-5H4" fill="none" stroke="#fff" stroke-width="1.6"/><circle cx="6" cy="10.5" r="1.3" fill="#fff"/><circle cx="11" cy="10.5" r="1.3" fill="#fff"/></svg>Checkout</a>
</nav>

<div class="layout">
  <aside class="sidebar">
    <section class="side-block">
      <h2 class="side-head"><svg width="20" height="16" viewBox="0 0 20 16"><circle cx="10" cy="14" r="2" fill="#fff"/><path d="M4 10a8 8 0 0 1 12 0M1 6.5a12.5 12.5 0 0 1 18 0" fill="none" stroke="#fff" stroke-width="2.2" stroke-linecap="round"/></svg>Broadcast</h2>
      <ul class="side-list">
        <li>Camvale</li><li>Portaguard</li><li>Pelton - Squall Cases</li><li>Pelton</li><li>Kavo</li><li>Petrax</li><li>CR Cases</li><li>ProSack</li><li>Dogleg Bag</li>
      </ul>
    </section>
    <section class="side-block">
      <h2 class="side-head"><svg width="18" height="15" viewBox="0 0 18 15"><path d="M1 3h4l1.5-2h5L13 3h4v11H1z" fill="#fff"/><circle cx="9" cy="8.5" r="3.2" fill="#2b2b2b"/></svg>Photography</h2>
      <ul class="side-list">
        <li>Pelton - Squall Cases</li><li>Vantor Hard Cases</li><li>Pelton</li><li>Kavo</li><li>Crumbrook</li><li>Billinford Bags</li><li>Lowfield</li><li>Tamwick</li>
      </ul>
    </section>
    <section class="side-block">
      <h2 class="side-head"><svg width="18" height="18" viewBox="0 0 18 18"><circle cx="9" cy="9" r="8" fill="#fff"/><rect x="8" y="7.5" width="2" height="6" fill="#2b2b2b"/><circle cx="9" cy="5" r="1.2" fill="#2b2b2b"/></svg>Information</h2>
      <ul class="side-list">
        <li>About Us</li><li>Pelton Case FAQ's</li><li>Pelton Size Guide</li><li>Privacy Policy</li><li>Shipping and Returns</li><li>Squall Case FAQ's</li><li>Terms &amp; Conditions</li>
      </ul>
    </section>
    <section class="side-block">
      <h2 class="side-head"><svg width="18" height="18" viewBox="0 0 18 18"><rect x="1" y="3" width="13" height="14" rx="1" fill="none" stroke="#fff" stroke-width="2"/><path d="M8 11l8-9 2 2-8 9H8z" fill="#fff"/></svg>Latest Post</h2>
      <div class="post"><div class="post-thumb">IMG1</div><div><p class="post-title">Duis sapien turpis nec.</p><p class="post-excerpt">Integer ornare libero nisi. Duis ac magna sit. Nulla facilis...</p></div></div>
      <div class="post"><div class="post-thumb">IMG1</div><div><p class="post-title">Duis sapien turpis nec.</p><p class="post-excerpt">Integer ornare libero nisi. Duis ac magna sit. Nulla facilis...</p></div></div>
      <div class="post"><div class="post-thumb">IMG1</div><div><p class="post-title">Duis sapien turpis nec.</p><p class="post-excerpt">Integer ornare libero nisi. Duis ac magna sit. Nulla facilis...</p></div></div>
    </section>
  </aside>

  <main class="main">
    <section class="hero">
      <div class="hero-photo" role="img" aria-label="Photo of a black messenger camera bag carried on a city street"></div>
      <div class="hero-shade"></div>
      <div class="hero-copy">
        <h2 class="hero-title">LOREM IPSUM IS SIMPLY</h2>
        <p class="hero-text">Lorem Ipsum is simply dummy text of the printing and typesetting industry. Lorem Ipsum</p>
        <p class="hero-price">£150</p>
        <p class="hero-shop">Shop Now ! <svg width="22" height="18" viewBox="0 0 14 12"><path d="M0 1h3l2 7h7l2-5H4" fill="none" stroke="#fff" stroke-width="1.6"/><circle cx="6" cy="10.5" r="1.3" fill="#fff"/><circle cx="11" cy="10.5" r="1.3" fill="#fff"/></svg></p>
      </div>
    </section>

    <section class="panel intro">
      <h1>Home</h1>
      <p>Gearcrate are a leading distributor to the film, television and photographic industries. We stock thousands of quality products from Pelton, Crumbrook, Billinford, Kavo, Metra, Slyde, Tamwick, Petrax, Portaguard, Tamlow, Lowfield, Vocan and other leading manufacturers. These products include:</p>
      <ul class="brand-list">
        <li><svg width="6" height="8" viewBox="0 0 6 8"><path d="M0 0l6 4-6 4z" fill="#333"/></svg>Pelton camera cases, Pelton director cases, Pelton projector cases and Pelton audio cases</li>
        <li><svg width="6" height="8" viewBox="0 0 6 8"><path d="M0 0l6 4-6 4z" fill="#333"/></svg>Crumbrook camera cases, Crumbrook laptop bags and Crumbrook bags</li>
        <li><svg width="6" height="8" viewBox="0 0 6 8"><path d="M0 0l6 4-6 4z" fill="#333"/></svg>Billinford camera bags, Billinford pockets and Billinford stowaway bags</li>
        <li><svg width="6" height="8" viewBox="0 0 6 8"><path d="M0 0l6 4-6 4z" fill="#333"/></svg>Kavo mixer cases, Kavo organiser bags, Kavo body armour and accessories</li>
        <li><svg width="6" height="8" viewBox="0 0 6 8"><path d="M0 0l6 4-6 4z" fill="#333"/></svg>Tamwick camera bags and Tamwick backpacks</li>
        <li><svg width="6" height="8" viewBox="0 0 6 8"><path d="M0 0l6 4-6 4z" fill="#333"/></svg>Petrax camera bags, Petrax camera covers and Petrax lighting bags</li>
        <li><svg width="6" height="8" viewBox="0 0 6 8"><path d="M0 0l6 4-6 4z" fill="#333"/></svg>Portaguard audio cases, Portaguard camera cases and Portaguard computer cases</li>
      </ul>
      <div class="delivery-badge" role="img" aria-label="Illustration of a delivery van announcing free delivery"></div>
    </section>

    <section class="panel featured">
      <h2 class="featured-head"><svg width="18" height="18" viewBox="0 0 18 18"><path d="M1 8h4v9H1zM6 8l4-7c1.5 0 2 1 2 2l-1 4h5c1 0 2 1 1.6 2.2l-2 6.8H6z" fill="none" stroke="#fff" stroke-width="1.6" stroke-linejoin="round"/></svg>Featured Products</h2>
      <div class="product-grid">
        <article class="product"><div class="product-photo" role="img" aria-label="Photo of a dark wheeled hard equipment case"></div><h3 class="product-name">Lorem Ipsum</h3><p class="product-desc">Lorem Ipsum doler sit&nbsp; Ipsum doler sit&nbsp; Ipsum doler sit</p><p class="product-price">Price <span>$4.25</span> (exc VAT)</p><a class="btn" href="#">More Info</a></article>
        <article class="product"><div class="product-photo" role="img" aria-label="Photo of a dark wheeled hard equipment case"></div><h3 class="product-name">Lorem Ipsum</h3><p class="product-desc">Lorem Ipsum doler sit&nbsp; Ipsum doler sit&nbsp; Ipsum doler sit</p><p class="product-price">Price <span>$4.25</span> (exc VAT)</p><a class="btn" href="#">More Info</a></article>
        <article class="product"><div class="product-photo" role="img" aria-label="Photo of a dark wheeled hard equipment case"></div><h3 class="product-name">Lorem Ipsum</h3><p class="product-desc">Lorem Ipsum doler sit&nbsp; Ipsum doler sit&nbsp; Ipsum doler sit</p><p class="product-price">Price <span>$4.25</span> (exc VAT)</p><a class="btn" href="#">More Info</a></article>
        <article class="product"><div class="product-photo" role="img" aria-label="Photo of a dark wheeled hard equipment case"></div><h3 class="product-name">Lorem Ipsum</h3><p class="product-desc">Lorem Ipsum doler sit&nbsp; Ipsum doler sit&nbsp; Ipsum doler sit</p><p class="product-price">Price <span>$4.25</span> (exc VAT)</p><a class="btn" href="#">More Info</a></article>
        <article class="product"><div class="product-photo" role="img" aria-label="Photo of a dark wheeled hard equipment case"></div><h3 class="product-name">Lorem Ipsum</h3><p class="product-desc">Lorem Ipsum doler sit&nbsp; Ipsum doler sit&nbsp; Ipsum doler sit</p><p class="product-price">Price <span>$4.25</span> (exc VAT)</p><a class="btn" href="#">More Info</a></article>
        <article class="product"><div class="product-photo" role="img" aria-label="Photo of a dark wheeled hard equipment case"></div><h3 class="product-name">Lorem Ipsum</h3><p class="product-desc">Lorem Ipsum doler sit&nbsp; Ipsum doler sit&nbsp; Ipsum doler sit</p><p class="product-price">Price <span>$4.25</span> (exc VAT)</p><a class="btn" href="#">More Info</a></article>
      </div>
    </section>
  </main>
</div>

<footer class="footer">
  <div class="footer-inner">
    <div class="footer-products">
      <h3>Our Products</h3>
      <ul>
        <li>Portaguard-cases</li><li>Petrax products</li><li>Kavo products</li><li>Vocan products</li><li>Pelton cases for the broadcast industry</li><li>Pelton cases for the photography industry</li>
      </ul>
    </div>
    <div class="footer-pay">
      <h3>Payment Methods</h3>
      <div class="pay-strip">
        <span class="pay-chip" style="width:120px;background:#e9eef4"></span>
        <span class="pay-chip" style="width:90px;background:#d7dde8"></span>
        <span class="pay-chip" style="width:110px;background:#f2d9b5"></span>
        <span class="pay-chip" style="width:50px;background:#1f3f8f"></span>
        <span class="pay-chip" style="width:50px;background:#1f3f8f"></span>
        <span class="pay-chip" style="width:50px;background:#1f3f8f"></span>
        <span class="pay-chip" style="width:46px;background:#3a6fc4"></span>
        <span class="pay-chip" style="width:46px;background:#e8a33a"></span>
      </div>
    </div>
    <p class="call">Order Online or Call: 01632 960400</p>
  </div>
  <div class="footer-rule"></div>
  <p class="copyright">© Copyright 2007 Gearcrate</p>
</footer>

</body>
</html>
```